Bluestone Freight

We are a 3PL freight brokerage company looking to create a website to attract new customers. Some ideas on how other freight websites look is located at these links, https://www.marigoldhaulerline.com/services, https://quillmarkcargo.com/freight-brokerage/.
We would like to have a quote feature implemented into this website.

We specialize in heavy-haul, specialized loads, flatbed, and dry vans.

```html
<!DOCTYPE html>
<html lang="en">
<head>
<meta charset="utf-8">
<title>Bluestone Freight</title>
<link rel="stylesheet" href="https://fonts.googleapis.com/css2?family=Montserrat:wght@400;500;600;700&display=swap">
<style>
:root{
  --navy:#1b365d;
  --navy-deep:#10203a;
  --gold:#b8962e;
  --ink:#1f2430;
  --muted:#5b6272;
  --line:#e3e6eb;
  --field:#f1f3f6;
  --soft:#eef1f4;
  --backdrop:#f4f5f7;
  --white:#ffffff;
}
*{box-sizing:border-box;margin:0;padding:0}
html,body{width:1200px;height:3707px;overflow:hidden}
body{background:var(--backdrop);font-family:'Montserrat',sans-serif;color:var(--ink)}
.page{position:absolute;left:35px;top:20px;width:1131px;background:var(--white)}
section,header,footer{position:relative;width:1131px;overflow:hidden}
.btn{display:inline-flex;align-items:center;justify-content:center;font-size:11px;font-weight:500;color:var(--white);height:32px;padding:0 12px;white-space:nowrap}
.btn-gold{background:var(--gold)}
.btn-navy{background:var(--navy)}

/* top bar */
.topbar{height:17px;background:var(--navy);display:flex;align-items:center;justify-content:space-between;padding:0 94px 0 86px;font-size:7px;color:var(--white)}
.dots{display:flex;gap:4px}
.dots span{width:6px;height:6px;border-radius:50%;background:var(--white)}
.topbar .contact{display:flex;gap:16px;align-items:center}
.topbar .contact span{display:flex;align-items:center;gap:3px}

/* nav */
.nav{height:57px;display:flex;align-items:center;justify-content:space-between;padding:0 94px 0 86px;border-bottom:1px solid var(--line)}
.brand{display:flex;align-items:center;gap:6px;font-weight:700;font-size:10px;color:var(--navy);letter-spacing:.5px}
.brand i{width:12px;height:12px;background:var(--navy);display:block}
.nav ul{display:flex;gap:22px;list-style:none;font-size:11px;margin-left:auto;margin-right:34px}
.nav .btn{height:33px;width:98px}

/* hero */
.hero{height:531px}
.hero .photo{position:absolute;inset:0;background:linear-gradient(180deg,#c9d6e3 0%,#a9bccd 28%,#48603a 40%,#2e4424 70%,#22331b 100%)}
.hero .copy{position:absolute;left:0;right:0;top:160px;text-align:center;color:var(--white)}
.hero h1{font-size:35px;font-weight:700;line-height:40px;width:420px;margin:0 auto}
.hero p{font-size:14px;line-height:17px;width:380px;margin:12px auto 0;font-weight:400}
.hero .actions{margin-top:22px;display:flex;justify-content:center;gap:4px}
.hero .actions .btn{width:135px}
.hero .actions .btn-gold{width:100px}

/* about */
.about{height:421px}
.about .photo{position:absolute;left:195px;top:87px;width:356px;height:245px;background:linear-gradient(180deg,#3a4e6e 0%,#d9a34e 45%,#55703a 65%,#3a4a32 100%)}
.about .copy{position:absolute;left:600px;top:96px;width:340px}
h2{font-size:26px;font-weight:700;color:var(--navy)}
.about p{font-size:10.5px;line-height:15px;color:var(--muted);margin-top:14px}
.about h4{font-size:13px;color:var(--navy);margin-top:20px}
.checks{display:grid;grid-template-columns:181px 1fr;row-gap:10px;margin-top:8px;font-size:10.5px;color:var(--muted);list-style:none}
.checks li{display:flex;align-items:center;gap:6px}

/* why */
.why{height:405px;background:var(--navy)}
.why .photo{position:absolute;inset:0}
.why .copy{position:absolute;left:164px;top:116px;width:340px;color:var(--white)}
.why h2{color:var(--white)}
.why p{font-size:10.5px;line-height:16px;margin-top:14px}
.why .btn{margin-top:26px;width:98px}

/* services */
.services{height:710px}
.services .intro{position:absolute;top:88px;left:0;right:0;text-align:center}
.services .intro p{font-size:11px;line-height:13px;width:370px;margin:12px auto 0;color:var(--ink)}
.grid{position:absolute;left:195px;top:228px;display:grid;grid-template-columns:356px 356px;column-gap:29px;row-gap:46px}
.card-img{height:118px}
.card h3{font-size:14px;font-weight:700;margin-top:22px}
.card p{font-size:9px;color:var(--muted);margin-top:7px}
.sky1{background:linear-gradient(180deg,#3d5479,#d2a056 50%,#5a7a3a)}
.sky2{background:linear-gradient(180deg,#c8ccd2,#9b2a2a 55%,#6b6a68)}
.sky3{background:linear-gradient(180deg,#c97f3e,#a2442e 50%,#8b5a36)}
.sky4{background:linear-gradient(180deg,#6f8db2,#cfd8e2 45%,#7a6a52)}

/* quote */
.quote{height:566px;background:var(--navy);color:var(--white)}
.quote .copy{position:absolute;left:195px;top:88px;width:330px}
.quote h2{color:var(--white);font-size:20px;line-height:26px}
.steps{list-style:none;margin-top:34px;position:relative}
.steps::before{content:"";position:absolute;left:8px;top:18px;height:155px;border-left:1px dashed rgba(255,255,255,.6)}
.steps li{display:flex;gap:20px;margin-bottom:36px;position:relative}
.steps svg{flex:none;background:var(--navy)}
.steps h3{font-size:14px;font-weight:700}
.steps p{font-size:9px;line-height:11px;margin-top:9px;width:240px}
.form{position:absolute;left:551px;top:45px;width:385px;height:466px;background:var(--white);border-radius:4px;padding:36px 29px;color:var(--ink)}
.form h3{font-size:16px;font-weight:600;color:var(--navy)}
.fields{display:grid;grid-template-columns:repeat(6,1fr);gap:10px 8px;margin-top:22px}
.fields span{height:29px;background:var(--field);font-size:8.5px;color:#9aa0ab;display:flex;align-items:center;padding-left:12px}
.c2{grid-column:span 2}.c3{grid-column:span 3}.c6{grid-column:span 6}
.form .btn{width:100%;margin-top:22px}

/* news */
.news{height:521px;background:var(--soft)}
.news .intro{position:absolute;top:60px;left:0;right:0;text-align:center}
.news .intro p{font-size:11px;line-height:15px;width:340px;margin:12px auto 0}
.posts{position:absolute;left:195px;top:147px;display:flex;gap:18px}
.post{width:235px;height:304px;background:var(--white)}
.post .img{height:177px}
.post .body{padding:14px 13px}
.post h3{font-size:12.5px;font-weight:700;line-height:14px}
.post time{display:block;font-size:6.5px;color:#9aa0ab;margin-top:7px}
.post p{font-size:7.5px;line-height:11px;color:var(--muted);margin-top:10px}

/* partners */
.partners{height:151px;display:flex;align-items:center;justify-content:space-around;padding:0 40px;font-size:12px;font-weight:600;color:#6b7280}
.partners .shape{width:30px;height:30px;background:#9ca3af}
.partners .disc{border-radius:50%}

/* footer */
.footer{height:293px;background:var(--navy-deep);color:var(--white)}
.footer .about-col{position:absolute;left:178px;top:44px;width:200px}
.footer .about-col .name{font-size:15px;font-weight:700;letter-spacing:1px}
.footer .about-col p{font-size:7.5px;line-height:11px;margin-top:28px;opacity:.85}
.footer .social{display:flex;gap:9px;margin-top:14px}
.footer .social span{width:10px;height:10px;border-radius:50%;background:var(--white)}
.col{position:absolute;top:88px;font-size:9.5px}
.col h4{font-size:10px;font-weight:700;margin-bottom:16px}
.col li{list-style:none;margin-bottom:16px;opacity:.9}
.footer hr{position:absolute;left:178px;right:178px;top:234px;border:0;border-top:1px solid rgba(255,255,255,.2)}
.footer .legal{position:absolute;left:0;right:0;top:266px;text-align:center;font-size:6.5px;opacity:.8}
</style>
</head>
<body>
<div class="page">
  <header>
    <div class="topbar">
      <div class="dots"><span></span><span></span><span></span><span></span></div>
      <div class="contact">
        <span><svg width="7" height="7" viewBox="0 0 10 10"><path d="M2 1l2 2-1 1.5a6 6 0 003 3L7.5 6l2 2-1.5 1.5C4 9 1 6 .5 1.5z" fill="#fff"/></svg>123-456-7890</span>
        <span><svg width="8" height="6" viewBox="0 0 10 7"><rect width="10" height="7" fill="#fff"/><path d="M0 0l5 4 5-4" stroke="#1b365d" fill="none"/></svg>info@bluestonefreight.com</span>
      </div>
    </div>
    <nav class="nav">
      <div class="brand"><i></i>BLUESTONE FREIGHT</div>
      <ul><li>Home</li><li>Services</li><li>About</li><li>Join Us</li><li>Contact Us</li></ul>
      <a class="btn btn-gold">Get Quote</a>
    </nav>
  </header>

  <section class="hero">
    <div class="photo" role="img" aria-label="Aerial view of a highway cutting through dense green forest under a cloudy sky"></div>
    <div class="copy">
      <h1>Lorem ipsum dolor sit amet, consetetur</h1>
      <p>Lorem ipsum dolor sit amet, consetetur sadipscing elitr, sed diam nonumy eirmod tempor</p>
      <div class="actions"><a class="btn btn-navy">Call (123) 123-4567</a><a class="btn btn-gold">Get Quote</a></div>
    </div>
  </section>

  <section class="about">
    <div class="photo" role="img" aria-label="Blue semi truck on a country road at sunset"></div>
    <div class="copy">
      <h2>About Bluestone Freight</h2>
      <p>Lorem Ipsum Dolor Sit Amet, Consetetur Sadipscing Elitr, Sed Diam Nonumy Eirmod Tempor Invidunt Ut Labore Et Dolore Magna Aliquyam Erat, Sed Diam Voluptua. At Vero Eos Et Accusam Et Justo Duo Dolores Et Ea Rebum. Stet Clita Kasd Gubergren, No Sea Takimata Sanctus</p>
      <h4>We...</h4>
      <ul class="checks">
        <li><svg width="9" height="9" viewBox="0 0 10 10"><path d="M1 5l3 3 5-6" stroke="#3c8a3c" stroke-width="1.6" fill="none"/></svg>Save Time</li>
        <li><svg width="9" height="9" viewBox="0 0 10 10"><path d="M1 5l3 3 5-6" stroke="#3c8a3c" stroke-width="1.6" fill="none"/></svg>Ship With Confidence</li>
        <li><svg width="9" height="9" viewBox="0 0 10 10"><path d="M1 5l3 3 5-6" stroke="#3c8a3c" stroke-width="1.6" fill="none"/></svg>Find Freight Easily</li>
        <li><svg width="9" height="9" viewBox="0 0 10 10"><path d="M1 5l3 3 5-6" stroke="#3c8a3c" stroke-width="1.6" fill="none"/></svg>Simply Process</li>
        <li><svg width="9" height="9" viewBox="0 0 10 10"><path d="M1 5l3 3 5-6" stroke="#3c8a3c" stroke-width="1.6" fill="none"/></svg>Protect Your Package</li>
        <li><svg width="9" height="9" viewBox="0 0 10 10"><path d="M1 5l3 3 5-6" stroke="#3c8a3c" stroke-width="1.6" fill="none"/></svg>Cost Reduction</li>
      </ul>
    </div>
  </section>

  <section class="why">
    <svg class="photo" width="1131" height="405" viewBox="0 0 1131 405" role="img" aria-label="Black and white photo of a white semi truck on a road beside railway tracks and water">
      <defs><linearGradient id="mono" x1="0" y1="0" x2="1" y2="1"><stop offset="0" stop-color="#8a8a8a"/><stop offset=".5" stop-color="#c9c9c9"/><stop offset="1" stop-color="#4a4a4a"/></linearGradient></defs>
      <path d="M641 0 Q500 202 641 405 L1131 405 L1131 0 Z" fill="url(#mono)"/>
    </svg>
    <div class="copy">
      <h2>Why Bluestone Freight</h2>
      <p>Lorem Ipsum Dolor Sit Amet, Consetetur Sadipscing Elitr, Sed Diam Nonumy Eirmod Tempor Invidunt Ut Labore Et Dolore Magna Aliquyam Erat, Sed Diam Voluptua.</p>
      <a class="btn btn-gold">Get Quote</a>
    </div>
  </section>

  <section class="services">
    <div class="intro">
      <h2>Our Services</h2>
      <p>Lorem Ipsum Dolor Sit Amet, Consetetur Sadipscing Elitr, Sed Diam Nonumy Eirmod Tempor Invidunt Ut Labore.</p>
      <p>Lorem Ipsum Dolor Sit Amet, Consetetur Sadipscing Elitr, Sed Diam Nonumy Eirmod Tempor Invidunt Ut Labore Dolore Magna</p>
    </div>
    <div class="grid">
      <article class="card"><div class="card-img sky1" role="img" aria-label="Blue truck on a rural road at sunset"></div><h3>Heavy-Haul</h3><p>Lorem Ipsum Dolor Sit Amet, Consetetur Sadipscing Elitr, Sed</p></article>
      <article class="card"><div class="card-img sky2" role="img" aria-label="Red semi truck parked at a depot"></div><h3>Specialized Loads</h3><p>Lorem Ipsum Dolor Sit Amet, Consetetur Sadipscing Elitr, Sed</p></article>
      <article class="card"><div class="card-img sky3" role="img" aria-label="Red truck driving under an orange evening sky"></div><h3>Flatbed</h3><p>Lorem Ipsum Dolor Sit Amet, Consetetur Sadipscing Elitr, Sed</p></article>
      <article class="card"><div class="card-img sky4" role="img" aria-label="White truck on an open desert highway"></div><h3>Dry Vans</h3><p>Lorem Ipsum Dolor Sit Amet, Consetetur Sadipscing Elitr, Sed</p></article>
    </div>
  </section>

  <section class="quote">
    <div class="copy">
      <h2>Searching for Freight Service? Here we are!</h2>
      <ul class="steps">
        <li><svg width="17" height="17" viewBox="0 0 18 18"><circle cx="9" cy="9" r="8" stroke="#fff" fill="none"/><path d="M5 9l3 3 5-6" stroke="#fff" fill="none"/></svg><div><h3>Flatbed</h3><p>Lorem Ipsum Dolor Amet, Consetetur Sadipscing Elitr, Sed</p></div></li>
        <li><svg width="17" height="17" viewBox="0 0 18 18"><circle cx="9" cy="9" r="8" stroke="#fff" fill="none"/><path d="M5 9l3 3 5-6" stroke="#fff" fill="none"/></svg><div><h3>Flatbed</h3><p>Lorem Ipsum Dolor Amet, Consetetur Sadipscing Elitr, Sed</p></div></li>
        <li><svg width="17" height="17" viewBox="0 0 18 18"><circle cx="9" cy="9" r="8" stroke="#fff" fill="none"/><path d="M5 9l3 3 5-6" stroke="#fff" fill="none"/></svg><div><h3>Flatbed</h3><p>Lorem Ipsum Dolor Amet, Consetetur Sadipscing Elitr, Sed</p></div></li>
      </ul>
    </div>
    <form class="form">
      <h3>Get a Freight Quote</h3>
      <div class="fields">
        <span class="c3">First Name</span><span class="c3">First Name</span>
        <span class="c3">Company</span><span class="c3">Phone</span>
        <span class="c6">Email</span>
        <span class="c6">Street Address</span>
        <span class="c2">City</span><span class="c2">State</span><span class="c2">Zip Code</span>
        <span class="c6">Shipment Type</span>
        <span class="c3">Origin City</span><span class="c3">Destination City</span>
        <span class="c6">Shipment Details</span>
      </div>
      <a class="btn btn-navy">Send Quote</a>
    </form>
  </section>

  <section class="news">
    <div class="intro">
      <h2>Company News</h2>
      <p>Lorem Ipsum Dolor Sit Amet, Consetetur Sadipscing Elitr, Sed Diam Nonumy Eirmod Tempor Invidunt</p>
    </div>
    <div class="posts">
      <article class="post"><div class="img sky1" role="img" aria-label="Blue truck on a rural road at sunset"></div><div class="body"><h3>Lorem Ipsum Dolor Sit Amet Consetetur Sadipscing.</h3><time>April 26, 2022</time><p>Lorem Ipsum Dolor Sit Amet, Consetetur Sadipscing Elitr, Sed Diam Nonumy Eirmod Tempor Invidunt Ut Labore Et Dolore Magna Aliquyam Erat...</p></div></article>
      <article class="post"><div class="img sky1" role="img" aria-label="Blue truck on a rural road at sunset"></div><div class="body"><h3>Lorem Ipsum Dolor Sit Amet Consetetur Sadipscing.</h3><time>April 26, 2022</time><p>Lorem Ipsum Dolor Sit Amet, Consetetur Sadipscing Elitr, Sed Diam Nonumy Eirmod Tempor Invidunt Ut Labore Et Dolore Magna Aliquyam Erat...</p></div></article>
      <article class="post"><div class="img sky1" role="img" aria-label="Blue truck on a rural road at sunset"></div><div class="body"><h3>Lorem Ipsum Dolor Sit Amet Consetetur Sadipscing.</h3><time>April 26, 2022</time><p>Lorem Ipsum Dolor Sit Amet, Consetetur Sadipscing Elitr, Sed Diam Nonumy Eirmod Tempor Invidunt Ut Labore Et Dolore Magna Aliquyam Erat...</p></div></article>
    </div>
  </section>

  <section class="partners">
    <span>Kelvora</span>
    <span>Sellnook</span>
    <span>Dunmere</span>
    <span class="shape"></span>
    <span>Ferncroft</span>
    <span>Cargelle</span>
    <span class="shape disc"></span>
    <span>Harrowby</span>
  </section>

  <footer class="footer">
    <div class="about-col">
      <div class="name">BLUESTONE FREIGHT</div>
      <p>Lorem Ipsum Dolor Sit Amet, Consetetur Sadipscing Elitr, Sed Diam Nonumy Eirmod Tempor Invidunt Ut Labore Et Dolore Magna Aliquyam Erat...</p>
      <div class="social"><span></span><span></span><span></span><span></span></div>
    </div>
    <div class="col" style="left:463px"><h4>Company</h4><ul><li>Home</li><li>About Us</li><li>Why Us</li><li>Join Us</li></ul></div>
    <div class="col" style="left:602px"><h4>Services</h4><ul><li>Heavy-Haul</li><li>Specialized Loads</li><li>Flatbed</li><li>Dry Vans</li></ul></div>
    <div class="col" style="left:769px"><h4>Contact Us</h4><ul><li>Bluestone Freight Add:<br><br>96 Lorem Ipsum Dolar, XYZ 12345</li><li>Phone: 123-456-7890</li><li>E-Mail: info@bluestonefreight.com</li></ul></div>
    <hr>
    <div class="legal">Bluestone Freight Copyright 2022 | All Rights Reserved. · Terms Of Use | Privacy Policy</div>
  </footer>
</div>
</body>
</html>
```